"VEX" Web Design Project

We need a create a webpage for a Streaming device product with sucription that we're going lo launch(like a lumo or pebble tv but comes with a possibily of monthly sucription of live tv channels).
The name of the product is "VEX" (vivid exchange viewing)

We are looking for something simple and with quality. Something webpages that we like are www.skyrune.com www.tindle.tv (our product will be very similar to tindle so you canuse for the menu an information reference, we're going to be more features because we are based on orbix so users can download all the apps from the marlow appmarket)
Also our remote control are gyroscopic (means like the zep remote) for many games.
We are working also in the logo so you can also see in our package and logo contest named: "HOME CAST UNIT: Box-unit-emblem" the Design #: 1768146 are the logo that maybe we're going to choose.

this is the link of our manufacturer to have on idea of the features of the device;
http://www.varnolux.com/pa/qbx730.asp

We like one color on the logo. But we want to see the logo in this colors: white,black ,light blue.

Thanks

Hi,
you can use for reference the TINDLE.TV webpage (look and feel, conten, information and & of pages..) also skyrune.tv as (look & feel).

Information to add:
In the case of the content the basic different is our device is orbix based. So only for reference of information to add (because we don't like lood and feel!!)  please use the info of  this links:

Spanish:
http://www.tolvaro.es/
products:
http://www.tolvaro.es/tolvaro-ZK830.html
http://www.tolvaro.es/descargas.html
http://www.tolvaro.es/about.html
http://www.tolvaro.es/contact.html
http://www.tolvaro.es/distribuidores.html

English:
http://www.tolvaro.com/product.asp?id=166
http://www.tolvaro.com/news.asp
http://www.tolvaro.com/support.asp
http://www.tolvaro.com/where-to-buy.asp
http://www.tolvaro.com/down.asp?id=1
http://www.tolvaro.com/about-us.asp

Note: are the same info but we're going to have only one model called: "VEX" . So we're going to by the devices to this manufacturer but we're going to rebranded...

AGAIN WE DON'T LIKE THE LOOK & FEEL OF THE LAST LINKS (ARE HORRIBLE) PLEASE USE AS A REFRENCE OF "LOOK & FEEL"  WWW.TINDLE.TV OR SKYRUNE.COM

https://www.filecrate-demo.net/sh/qx8831pwwr7mbel/R29KdTesoq

This files can help for the branding and pictures

Can you change the photos of the Slatex's per someone looking TV? One of the advantage of our product vrs conventional tv cable service is that we are Unplugged , we are Cord cutters. With our VEX device people can see TV on their home, their office, their vacation home. Because they can tke with them our device and conect to the internet and can see TV. 
Another advantage if for exmple our partnership with http://www.castorelay.tv/ so people can use their smartphones and tables as a remote control. But not normal remote control, totally interactive remote control and can share also all the network, my phone, and internet content to the TV by our VEX device. 

Please see the attached file. you can use something similar...

Target Market(s)

under 40 years. young people.

Industry/Entity Type

Tv

```html
<!DOCTYPE html>
<html lang="es">
<head>
<meta charset="utf-8">
<title>VEX Streaming device</title>
<link rel="stylesheet" href="https://fonts.googleapis.com/css2?family=Arimo:wght@400;700&display=swap">
<style>
:root{
  --bar:#3a3a3a;
  --band:#3e3e3e;
  --blue:#0ba6ee;
  --ink:#111;
  --soft:#555;
  --panel:#f3f3f3;
  --white:#fff;
  --font:"Arimo", Arial, sans-serif;
}
*{margin:0;padding:0;box-sizing:border-box}
html,body{width:1200px;height:2215px;overflow:hidden;font-family:var(--font);color:var(--ink);background:#f7f7f7}
.page{position:relative;width:1200px;height:2215px}
.abs{position:absolute}
.site-header{left:0;top:0;width:1200px;height:68px;background:var(--bar)}
.brand{left:114px;top:14px;color:var(--white);font-weight:700;font-size:34px;letter-spacing:1px;display:flex;align-items:center;gap:8px}
.brand-dot{width:14px;height:14px;border-radius:50%;background:var(--white)}
.hero{left:0;top:68px;width:1200px;height:587px}
.hero-photo{position:absolute;inset:0;background:linear-gradient(100deg,#d8d6d2 0%,#c9c7c3 35%,#8f8f8f 50%,#4a4a4a 62%,#c7c5c1 80%,#e2e0dc 100%)}
.hero-title{left:116px;top:254px;color:var(--white);font-size:36px}
.hero-title b{font-weight:700}
.hero-sub{left:116px;top:312px;color:#333;font-size:24px;line-height:29px}
.hero-link{left:116px;top:400px;color:var(--blue);font-size:19px}
.btn-primary{left:116px;top:445px;width:178px;height:52px;background:var(--blue);color:var(--white);font-size:19px;display:flex;align-items:center;justify-content:center}
.welcome{left:0;top:655px;width:1200px;height:360px;background:var(--white)}
.welcome-title{left:116px;top:60px;font-size:40px;font-weight:400}
.welcome-title b{font-weight:700}
.welcome-text{left:116px;top:117px;width:520px;font-size:18.5px;line-height:33px}
.welcome-logo{left:858px;top:70px;font-size:50px;font-weight:700;color:#555;letter-spacing:2px}
.device-photo{left:785px;top:157px;width:271px;height:144px;background:linear-gradient(180deg,#2a2a2a 0%,#111 70%,#e4e4e4 72%,#cfcfcf 100%);border-radius:10px}
.features{left:0;top:1015px;width:1200px;height:397px;background:var(--panel)}
.side-photo{left:157px;top:28px;width:92px;height:332px;background:linear-gradient(90deg,#e8e8e8 0%,#e8e8e8 25%,#222 26%,#111 100%);border-radius:6px}
.features-title{left:0;width:1200px;top:60px;text-align:center;padding-left:60px;color:var(--blue);font-size:37px}
.feature-list{list-style:none;font-size:11px;color:#333;line-height:24.6px;text-transform:uppercase}
.col-a{left:329px;top:138px}
.col-b{left:687px;top:138px}
.needs{left:0;top:1412px;width:1200px;height:375px;background:linear-gradient(180deg,#fff,#f4f4f4)}
.needs h3{font-size:23px;font-weight:700}
.needs-left{left:150px;top:60px}
.needs-left ul{list-style:none;margin-top:12px;font-size:16px;color:#444;line-height:29px}
.needs-mid{left:437px;top:60px}
.needs-mid ul{list-style:none;margin-top:10px;font-size:19px;color:#333;line-height:29px}
.needs-note{left:428px;top:222px;color:var(--blue);font-size:13px;line-height:18px;display:flex;gap:6px}
.needs-note span:first-child{font-size:30px;line-height:30px}
.box-photo{left:766px;top:37px;width:286px;height:268px;background:linear-gradient(160deg,#3a3a3a 0%,#1c1c1c 60%,#2c2c2c 100%);clip-path:polygon(20% 0,100% 18%,82% 100%,0 78%)}
.steps{left:0;top:1787px;width:1200px;height:216px;background:var(--band);color:var(--white)}
.step-divider{top:0;width:2px;height:216px;background:#2e2e2e}
.step-num{width:30px;height:30px;border-radius:50%;background:var(--blue);color:var(--white);font-weight:700;font-size:18px;display:flex;align-items:center;justify-content:center}
.step-label{font-size:24px;line-height:28px}
.cta{left:0;top:2003px;width:1200px;height:105px;background:var(--blue)}
.cta-text{left:0;width:834px;top:30px;text-align:center;color:var(--white);font-size:37px}
.btn-buy{left:700px;top:30px;width:218px;height:53px;background:var(--bar);color:var(--white);font-size:28px;display:flex;align-items:center;justify-content:center;gap:8px}
.btn-buy b{font-weight:700}
</style>
</head>
<body>
<div class="page">
  <header class="site-header abs">
    <div class="brand abs"><span class="brand-dot"></span>VEX</div>
  </header>

  <section class="hero abs">
    <div class="hero-photo" role="img" aria-label="Product photo: remote control with keyboard leaning on the packaged streaming box on a light table"></div>
    <h1 class="hero-title abs"><b>VEX</b> Streaming device</h1>
    <p class="hero-sub abs">Stream TV &amp; recordings<br>to any device.</p>
    <p class="hero-link abs">Lorem ipsum dolor sit amen</p>
    <a class="btn-primary abs">Lorem Ipsum</a>
  </section>

  <section class="welcome abs">
    <h2 class="welcome-title abs">Welcome to <b>VEX</b></h2>
    <p class="welcome-text abs">Lorem ipsum dolor sit amet, consectetur adipisicing elit, sed do eiusmod tempor incididunt ut labore et dolore magna aliqua. Ut enim ad minim veniam, quis nostrud exercitation ullamco laboris nisi ut aliquip ex ea commodo consequat.</p>
    <div class="welcome-logo abs">VEX</div>
    <div class="device-photo abs" role="img" aria-label="Photo of the black streaming box"></div>
  </section>

  <section class="features abs">
    <div class="side-photo abs" role="img" aria-label="Side view of the box showing its ports"></div>
    <h2 class="features-title abs">Caracteristicas</h2>
    <ul class="feature-list abs col-a">
      <li>-Orbix 4.1</li>
      <li>-Video full 1080p HD (arriba de 4MB)</li>
      <li>-Control remoto con puntero "air mouse"</li>
      <li>-Dos entradas USB para accesorios y memoria</li>
      <li>-Entrada SD card</li>
      <li>-Memoria interna 8GB</li>
      <li>-Capacidad memoria externa 32GB</li>
      <li>-Navegador Quilla Browser</li>
    </ul>
    <ul class="feature-list abs col-b">
      <li>-Conexion cable ethernet 10/100M</li>
      <li>-Soporta camara USB para videollamadas</li>
      <li>-WiFi 802.11b/g/n</li>
      <li>-Memoria flash 2GB</li>
      <li>-Marlow Appmarket para miles aplicaciones</li>
      <li>-Aplicacion de control remoto en tu telefono*</li>
      <li>-Certificado Sonara Digital sound</li>
      <li>-Interactua con todos los dispositivos en mi red local*</li>
    </ul>
  </section>

  <section class="needs abs">
    <div class="needs-left abs">
      <h3>QUE&nbsp; NECESITO ?</h3>
      <ul>
        <li>- una TV con conexion HDMI</li>
        <li>- una conexion de internet</li>
        <li>&nbsp;(inhalambrico o por cable)</li>
      </ul>
    </div>
    <div class="needs-mid abs">
      <h3>QUE INCLUYE EL VEX TV&nbsp; ?</h3>
      <ul>
        <li>- un control remoto</li>
        <li>- un cable HDMI</li>
        <li>-&nbsp; adaptor de carroente</li>
        <li>- 12 meses de garantia</li>
      </ul>
    </div>
    <p class="needs-note abs"><span>*</span><span>(RECOMENDAMOS CONEXION<br>POR CABLE SOBRE 2MB MINIMO)</span></p>
    <div class="box-photo abs" role="img" aria-label="Photo of the open black product box with the device inside"></div>
  </section>

  <section class="steps abs">
    <div class="step-divider abs" style="left:486px"></div>
    <div class="step-divider abs" style="left:805px"></div>

    <div class="step-num abs" style="left:141px;top:34px">1</div>
    <p class="step-label abs" style="left:190px;top:22px">Conectalo a la energia<br>y Tv</p>
    <svg class="abs" style="left:225px;top:88px" width="180" height="110" viewBox="0 0 180 110" fill="none" stroke="#fff" stroke-width="3">
      <rect x="6" y="14" width="58" height="26" rx="8"/>
      <path d="M74 28h26m-8-7 8 7-8 7"/>
      <rect x="110" y="6" width="50" height="32" rx="3"/>
      <text x="120" y="30" fill="#fff" stroke="none" font-family="Arimo, sans-serif" font-size="17" font-weight="700">TV</text>
      <path d="M126 38v6h18v-6"/>
      <rect x="90" y="58" width="42" height="42" rx="9" fill="#fff"/>
      <rect x="103" y="70" width="4" height="9" fill="#3e3e3e" stroke="none"/>
      <rect x="115" y="70" width="4" height="9" fill="#3e3e3e" stroke="none"/>
      <rect x="108" y="84" width="6" height="5" fill="#3e3e3e" stroke="none"/>
    </svg>

    <div class="step-num abs" style="left:520px;top:34px">2</div>
    <p class="step-label abs" style="left:581px;top:34px">Agregalo a tu red</p>
    <svg class="abs" style="left:535px;top:112px" width="240" height="80" viewBox="0 0 240 80" fill="none" stroke="#fff" stroke-width="4" stroke-linecap="round">
      <path d="M8 20a36 36 0 0 1 48 0M16 30a24 24 0 0 1 32 0M24 40a12 12 0 0 1 16 0"/>
      <circle cx="32" cy="48" r="3" fill="#fff"/>
      <text x="10" y="72" fill="#fff" stroke="none" font-family="Arimo, sans-serif" font-size="13">Wi-Fi</text>
      <text x="98" y="48" fill="#fff" stroke="none" font-family="Arimo, sans-serif" font-size="15" font-style="italic">OR</text>
      <rect x="172" y="10" width="40" height="40" rx="4" stroke-width="3"/>
      <path d="M182 20h20v20h-20z M186 20v-4h12v4" stroke-width="2"/>
      <text x="166" y="72" fill="#fff" stroke="none" font-family="Arimo, sans-serif" font-size="10">ETHERNET</text>
    </svg>

    <div class="step-num abs" style="left:843px;top:34px">3</div>
    <p class="step-label abs" style="left:900px;top:34px">Disfrutalo!</p>
    <svg class="abs" style="left:890px;top:92px" width="124" height="106" viewBox="0 0 124 106" fill="none" stroke="#fff" stroke-width="3">
      <rect x="4" y="4" width="116" height="76"/>
      <path d="M62 80v14M36 98h52"/>
      <text x="33" y="54" fill="#fff" stroke="none" font-family="Arimo, sans-serif" font-size="28" font-weight="700">VEX</text>
    </svg>
  </section>

  <section class="cta abs">
    <p class="cta-text abs">Get Yours Right Now!</p>
    <a class="btn-buy abs">Buy <b>VEX</b></a>
  </section>
</div>
</body>
</html>
```